Commercial and Multifamily informational website

We need a website for our commercial real estate management company. We will manage offices, retail, apartments and others. Here is the brief verbiage: Providing quality commercial and multifamily portfolio management to Landlords, REITs, and financial institutions. 

Industry/Entity Type

Real Estate

Number of Pages Required

2 page

Font styles to use
Sans Serif
Other font styles liked:
• Muli, Garamond

Colors
0555a3
5c5c5c
3176b5
85acd3
474747

Requirements
Must have
• Home page and contact page

```html
<!DOCTYPE html>
<html lang="en">
<head>
<meta charset="utf-8">
<title>KVL Real Estate Management</title>
<link href="https://fonts.googleapis.com/css2?family=Lato:wght@400;700&family=Open+Sans:wght@600;700&display=swap" rel="stylesheet">
<style>
:root{
  --navy:#0a2b6e;
  --navy-deep:#062160;
  --blue:#0555a3;
  --blue-mid:#3176b5;
  --blue-light:#85acd3;
  --ink:#333333;
  --grey-text:#5c5c5c;
  --heading:#474747;
  --band:#f3f3f3;
  --white:#ffffff;
  --footer:#242424;
  --footer-line:#3a3a3a;
  --field:#1a1a1a;
  --screen-top:#8a9aa6;
  --screen-mid:#4f6048;
  --screen-low:#3d5233;
}
*{margin:0;padding:0;box-sizing:border-box}
html,body{width:1200px;height:2273px;overflow:hidden}
body{font-family:"Lato",sans-serif;color:var(--ink);background:var(--white)}
.wrap{width:1040px;margin:0 auto;position:relative}

.topbar{height:35px;background:var(--navy);color:var(--white);font-size:14px}
.topbar .wrap{display:flex;align-items:center;height:35px}
.topbar .item{display:flex;align-items:center;gap:8px;margin-right:40px}
.topbar .social{margin-left:auto;display:flex;gap:16px}
.topbar .social span{width:10px;height:10px;border-radius:50%;background:var(--white)}

.header{height:91px;background:var(--white)}
.header .wrap{display:flex;align-items:center;height:91px}
.brand{display:flex;align-items:center;gap:10px;font-family:"Lato",sans-serif;font-weight:700;color:var(--blue);font-size:20px;letter-spacing:.5px;white-space:nowrap}
.brand .mark{width:22px;height:22px;background:var(--blue);flex:none}
.nav{margin-left:auto;display:flex;gap:68px;font-size:17px;font-weight:700;color:var(--grey-text)}
.nav .active{color:var(--navy);border-bottom:2px solid var(--navy)}

.hero{height:377px;position:relative;background:linear-gradient(180deg,#2e6fd6 0%,#1a4aa8 55%,#0d2f7a 100%);color:var(--white)}
.hero .arrow{position:absolute;top:174px}
.hero .arrow.left{left:34px}
.hero .arrow.right{right:34px}
.hero h1{position:absolute;left:83px;top:290px;font-family:"Open Sans",sans-serif;font-weight:700;font-size:23px;line-height:33px;letter-spacing:.6px}
.btn-outline{position:absolute;right:124px;top:302px;width:170px;height:46px;border:2px solid var(--white);display:flex;align-items:center;justify-content:center;font-family:"Open Sans",sans-serif;font-weight:700;font-size:14px;letter-spacing:2px}

.title{text-align:center;font-family:"Open Sans",sans-serif;font-weight:700;font-size:36px;color:#2d2d2d}
.title em{font-style:normal;color:var(--navy)}
.rule{margin:6px auto 0;height:3px;border-top:1px solid #9a9a9a;border-bottom:1px solid #9a9a9a}

.services{height:406px;background:var(--band);padding-top:32px}
.services .intro{width:900px;margin:36px auto 0;text-align:center;font-size:15px;line-height:23px;color:var(--ink)}
.service-grid{display:flex;justify-content:space-between;margin-top:34px}
.service{width:230px;text-align:center}
.service .icon{width:70px;height:72px;margin:0 auto;background:var(--navy);border-radius:6px}
.service h3{margin-top:10px;font-size:18px;font-weight:700;color:var(--heading);letter-spacing:.5px}
.service p{margin-top:10px;font-size:15px;line-height:22px;color:var(--grey-text)}

.welcome{height:324px;padding-top:45px;text-align:center}
.welcome .title{display:flex;justify-content:center;align-items:center;gap:12px;color:var(--heading)}
.welcome .title .name{font-family:"Open Sans",sans-serif;color:var(--blue);font-size:22px}
.welcome p{width:1040px;margin:30px auto 0;font-size:15px;line-height:23px}
.btn-dark{display:inline-flex;margin-top:38px;width:135px;height:46px;border:2px solid var(--navy);align-items:center;justify-content:center;font-family:"Open Sans",sans-serif;font-weight:700;font-size:14px;letter-spacing:2px;color:var(--ink)}

.video{height:684px;background:linear-gradient(180deg,#ebebeb,#f2f2f2);padding-top:44px;position:relative}
.video p{width:1040px;margin:36px auto 0;text-align:center;font-size:16px;line-height:29px}
.video-screen{position:absolute;left:333px;top:273px;width:534px;height:332px;border-radius:4px;background:linear-gradient(180deg,var(--screen-top) 0%,#6f7f86 30%,var(--screen-mid) 65%,var(--screen-low) 100%);display:flex;align-items:center;justify-content:center}
.play{width:52px;height:52px}

.footer{height:306px;background:var(--footer);color:var(--white)}
.footer .wrap{display:flex;padding-top:38px}
.footer h4{font-size:18px;font-weight:700;padding-bottom:10px;border-bottom:1px solid var(--footer-line);margin-bottom:14px}
.col-links{width:135px;margin-right:64px}
.col-links li{list-style:none;font-size:14px;margin-bottom:22px}
.col-contact{width:250px;margin-right:66px;font-size:14px;line-height:21px}
.col-contact .row{display:flex;align-items:center;gap:14px;margin-top:16px}
.col-form{width:268px}
.field{height:35px;background:var(--field);border:1px solid #444;margin-bottom:7px;padding:8px 12px;font-size:14px;font-weight:700}
.field.tall{height:43px}
.submit{display:inline-block;margin-top:4px;background:var(--navy);padding:8px 22px;font-family:"Open Sans",sans-serif;font-weight:700;font-size:14px;letter-spacing:2px}
.col-brand{margin-left:auto;width:215px;padding-top:68px;text-align:center}
.col-brand .brand{color:#cfcfcf;font-size:15px;justify-content:center;gap:8px;letter-spacing:0}
.col-brand .brand .mark{width:16px;height:16px;background:#cfcfcf}
.circles{display:flex;justify-content:center;gap:6px;margin-top:36px}
.circles span{width:30px;height:30px;border-radius:50%;background:var(--blue-mid);border:2px solid var(--white)}

.copyright{height:50px;background:var(--navy);color:var(--white);font-size:13px;display:flex;align-items:center;justify-content:center}
</style>
</head>
<body>
<div class="topbar"><div class="wrap">
  <div class="item"><svg width="14" height="14" viewBox="0 0 24 24"><path fill="#fff" d="M6.6 10.8a15 15 0 0 0 6.6 6.6l2.2-2.2c.3-.3.7-.4 1-.2 1.1.4 2.3.6 3.6.6.6 0 1 .4 1 1V20c0 .6-.4 1-1 1A17 17 0 0 1 3 4c0-.6.4-1 1-1h3.5c.6 0 1 .4 1 1 0 1.3.2 2.5.6 3.6.1.3 0 .7-.2 1z"/></svg>123-456-7890</div>
  <div class="item"><svg width="14" height="11" viewBox="0 0 14 11"><rect width="14" height="11" fill="#fff"/><path d="M0 0l7 6 7-6" stroke="#0a2b6e" fill="none"/></svg>info@kvlpropertygroup.com</div>
  <div class="social"><span></span><span></span><span></span><span></span></div>
</div></div>

<header class="header"><div class="wrap">
  <div class="brand"><span class="mark"></span>KVL Real Estate Management</div>
  <nav class="nav"><span class="active">HOME</span><span>ABOUT</span><span>SERVICES</span><span>CONTACT</span></nav>
</div></header>

<section class="hero" role="img" aria-label="Illustrated blue city skyline of office towers at night">
  <svg class="arrow left" width="14" height="24" viewBox="0 0 14 24"><path d="M12 2L2 12l10 10" stroke="#fff" stroke-width="3" fill="none"/></svg>
  <svg class="arrow right" width="14" height="24" viewBox="0 0 14 24"><path d="M2 2l10 10L2 22" stroke="#fff" stroke-width="3" fill="none"/></svg>
  <h1>PROVIDING QUALITY COMMERCIAL &amp; MULTIFAMILY PORTFOLIO<br>MANAGEMENT TO LANDLORDS, REITS, &amp; FINANCIAL INSTITUTIONS.</h1>
  <div class="btn-outline">CONTACT NOW!</div>
</section>

<section class="services">
  <h2 class="title">OUR <em>SERVICES</em></h2>
  <div class="rule" style="width:265px"></div>
  <p class="intro">Duis autem vel eum iriure dolor in hendrerit in vulputate velit esse molestie consequat, vel illum dolore eu feugiat nulla facilisis at vero eros et accumsan et iusto odio dignissim qui blandit delenit augue duis dolore te feugait nulla facilisi.</p>
  <div class="wrap service-grid">
    <div class="service"><div class="icon" role="img" aria-label="Office worker at desk icon"></div><h3>MANAGE OFFICES</h3><p>Sed ut perspiciatis unde omnis iste natus error sdoloremque.</p></div>
    <div class="service"><div class="icon" role="img" aria-label="Retail storefront icon"></div><h3>RETAIL</h3><p>Sed ut perspiciatis unde omnis iste natus error sdoloremque.</p></div>
    <div class="service"><div class="icon" role="img" aria-label="Apartment building icon"></div><h3>APARTMENTS</h3><p>Sed ut perspiciatis unde omnis iste natus error sdoloremque.</p></div>
    <div class="service"><div class="icon" role="img" aria-label="Garage building icon"></div><h3>OTHER PROPERTIES</h3><p>Sed ut perspiciatis unde omnis iste natus error sdoloremque.</p></div>
  </div>
</section>

<section class="welcome">
  <h2 class="title">WELCOME TO <span class="name">KVL Real Estate Management</span></h2>
  <div class="rule" style="width:455px;border-color:var(--blue-light)"></div>
  <p>Lorem ipsum dolor sit amet, consectetur adipiscing elit, sed do eiusmod tempor incididunt ut labore et dolore magna aliqua. Ut enim &nbsp;veniam, quis nostrud exercitation ullamco laboris nisi ut aliquip ex ea commodo consequat. Duis aute irure dolor in reprehenderit in voluptate velit esse cillum xerci tation ullamcorper suscipit lobortis nisl ut aliquip ex ea commodo consequat. Duis m iriure dolor in</p>
  <span class="btn-dark">READ MORE</span>
</section>

<section class="video">
  <h2 class="title">WATCH <em>VIDEO</em></h2>
  <div class="rule" style="width:268px"></div>
  <p>Integrated warehousing and distribution services provide solutions that are tailor-made to your individual requirements, allowing you to achieve<br>seamlessly efficient transfers to your customers.</p>
  <div class="video-screen" role="img" aria-label="Video still of a suburban house with a front garden">
    <svg class="play" viewBox="0 0 52 52" aria-hidden="true"><circle cx="26" cy="26" r="26" fill="#e6e6e6" fill-opacity=".85"/><path d="M21 16l15 10-15 10z" fill="#333"/></svg>
  </div>
</section>

<footer class="footer"><div class="wrap">
  <div class="col-links"><h4>QUICK LINKS</h4><ul><li>• Home</li><li>• About</li><li>• Services</li><li>• Contact</li></ul></div>
  <div class="col-contact"><h4>CONTACT DETAILS</h4>
    <strong>KVL Real Estate Management</strong><br>123-Ut wisi enim ad minim veniam,<br>Link Road, NY - 123456
    <div class="row"><svg width="13" height="13" viewBox="0 0 24 24"><path fill="#fff" d="M6.6 10.8a15 15 0 0 0 6.6 6.6l2.2-2.2c.3-.3.7-.4 1-.2 1.1.4 2.3.6 3.6.6.6 0 1 .4 1 1V20c0 .6-.4 1-1 1A17 17 0 0 1 3 4c0-.6.4-1 1-1h3.5c.6 0 1 .4 1 1 0 1.3.2 2.5.6 3.6.1.3 0 .7-.2 1z"/></svg>123-456-7890</div>
    <div class="row"><svg width="13" height="13" viewBox="0 0 14 14"><rect x="3" y="0" width="8" height="4" fill="#fff"/><rect x="0" y="5" width="14" height="6" fill="#fff"/><rect x="3" y="9" width="8" height="5" fill="#fff" stroke="#242424"/></svg>123-456-7890</div>
    <div class="row"><svg width="13" height="10" viewBox="0 0 14 11"><rect width="14" height="11" fill="#fff"/><path d="M0 0l7 6 7-6" stroke="#242424" fill="none"/></svg>info@kvlpropertygroup.com</div>
  </div>
  <div class="col-form"><h4>QUICK &nbsp;INQUIRY</h4>
    <div class="field">Name</div><div class="field">Email</div><div class="field tall">Message</div>
    <span class="submit">SUBMIT</span>
  </div>
  <div class="col-brand">
    <div class="brand"><span class="mark"></span>KVL Real Estate Management</div>
    <div class="circles"><span></span><span></span><span></span></div>
  </div>
</div></footer>

<div class="copyright">Copyright © 2017 &nbsp;KVL Real Estate Management. All Right Reserved</div>
</body>
</html>
```